Basic Company webpage with the elements and colors of our Logo

Basic Home page with a few pages:
- Home,
- About US,
- Contact us
- Services

Target Market(s)

Business Customers (B2B)

Coding

Coded - Design and coding required

Number of Pages Required

5+ page

Requirements
Must have
• Professional, Clean, Simple High Tech, Contact should have a contact us dialog for sending messages to us
Nice to have
• Meet with us links for calendar access though MS Bookings

```html
<!DOCTYPE html>
<html lang="en">
<head>
<meta charset="utf-8">
<title>Nova Technology Services</title>
<link href="https://fonts.googleapis.com/css2?family=Poppins:wght@400;500;600;700&display=swap" rel="stylesheet">
<style>
:root{
  --navy:#0b4a6c;
  --orange:#f7a935;
  --ink:#222222;
  --text:#3a3a3a;
  --field:#eeeeee;
  --card-shadow:0 6px 24px rgba(20,40,60,.10);
}
*{box-sizing:border-box;margin:0;padding:0}
html,body{width:1200px;height:3267px;overflow:hidden}
body{position:relative;font-family:"Poppins",sans-serif;color:var(--text);background:#fff}
.abs{position:absolute}
a{text-decoration:none}

/* header */
.hero-bg{left:0;top:0;width:1200px;height:660px;background:linear-gradient(180deg,#eef3f6 0%,#f5f8fa 70%,#fff 100%)}
.globe{left:323px;top:76px;width:552px;height:564px;border-radius:50%;
  background:radial-gradient(circle at 50% 42%,rgba(255,255,255,.95) 0%,rgba(230,240,243,.85) 42%,rgba(150,196,210,.6) 78%,rgba(70,145,172,.55) 100%)}
.logo{left:89px;top:36px;display:flex;align-items:center;gap:8px;font-weight:700;font-size:25px;color:var(--navy);letter-spacing:.5px}
.logo .dot{width:14px;height:14px;border-radius:50%;background:var(--orange)}
.nav{top:41px;font-size:13px;font-weight:600;color:var(--ink);letter-spacing:.2px;line-height:20px}
.nav.active{color:var(--orange)}
.btn{display:flex;align-items:center;justify-content:center;border-radius:20px;font-weight:600;color:#fff;font-size:13px;height:38px}
.btn.orange{background:var(--orange)}
.btn.navy{background:var(--navy)}

.hero-title{left:0;width:1200px;top:276px;text-align:center;font-weight:700;font-size:43px;line-height:45px;color:var(--navy);letter-spacing:.3px}
.hero-sub{left:0;width:1200px;top:372px;text-align:center;font-size:16px;color:var(--ink)}

/* about */
.about-photo{left:152px;top:647px;width:432px;height:432px;border-radius:50%;
  background:radial-gradient(circle at 62% 55%,#a9b6c4 0%,#7d97b2 30%,rgba(80,120,160,0) 60%),linear-gradient(135deg,#2f7fa6 0%,#5d8fb4 45%,#3e5f88 100%)}
.about-kicker{left:630px;top:778px;font-size:22px;font-weight:700;color:var(--navy)}
.about-title{left:630px;top:808px;font-size:41px;line-height:45px;font-weight:700;color:var(--navy)}
.about-text{left:630px;top:905px;width:432px;font-size:15px;line-height:24px;color:var(--ink)}

/* services */
.section-title{left:0;width:1200px;text-align:center;font-weight:700;font-size:40px;color:var(--ink)}
.card{width:297px;height:248px;background:#fff;border-radius:20px;box-shadow:var(--card-shadow);padding:25px 35px}
.card.active{border-bottom:4px solid var(--navy)}
.card .icon{width:60px;height:60px;border-radius:50%;background:var(--orange);margin-bottom:24px;display:flex;align-items:center;justify-content:center}
.card .icon.navy{background:var(--navy)}
.card .icon svg{width:32px;height:32px;fill:none;stroke:#fff;stroke-width:1.6;stroke-linecap:round;stroke-linejoin:round}
.card h3{font-size:22px;font-weight:600;color:var(--ink);line-height:26px;margin-left:6px}
.card p{font-size:15.5px;line-height:21.5px;color:var(--text);margin-left:6px;margin-top:4px;white-space:nowrap}

/* who we serve */
.serve-photo{left:0;top:1787px;width:1200px;height:490px;
  background:
    radial-gradient(ellipse 170px 210px at 860px 300px,#f4f3ef 0%,#e9e6df 55%,rgba(233,230,223,0) 100%),
    radial-gradient(ellipse 120px 90px at 880px 130px,#c9a990 0%,rgba(201,169,144,0) 100%),
    radial-gradient(ellipse 170px 90px at 640px 390px,#e4e4e6 0%,rgba(228,228,230,0) 100%),
    linear-gradient(90deg,#ffffff 0%,#fbfbfa 34%,#e7e5e0 50%,#cfcbc2 66%,#b9b2a5 82%,#6e675c 100%)}
.serve-title{left:142px;top:1964px;font-size:40px;font-weight:700;color:var(--ink)}
.serve-text{left:142px;top:2020px;width:410px;font-size:15.5px;line-height:24px;color:var(--ink)}

/* contact */
.contact-sub{left:0;width:1200px;top:2413px;text-align:center;font-size:15.5px;line-height:24px;color:var(--ink)}
.field{background:var(--field);font-size:17px;color:#6a6a6a;padding:0 23px;display:flex;align-items:center}
.field.area{align-items:flex-start;padding-top:14px}

/* footer */
.footer{left:0;top:2897px;width:1200px;height:370px}
.f-logo{left:99px;top:3052px;display:flex;align-items:center;gap:8px;font-weight:700;font-size:25px;color:#fff;letter-spacing:.5px}
.f-logo .dot{width:14px;height:14px;border-radius:50%;background:var(--orange)}
.f-head{font-size:17px;font-weight:600;color:#fff}
.f-links{left:425px;list-style:none;font-size:13.5px;line-height:24px;color:#fff}
.f-links li:first-child{color:var(--orange)}
.f-contact{left:638px;list-style:none;font-size:15.5px;line-height:24px;color:#fff}
.f-contact li{display:flex;align-items:center;gap:16px}
.social{top:3052px;width:20px;height:20px;border-radius:50%;background:#fff}
.rule{left:89px;top:3212px;width:1022px;height:1px;background:rgba(255,255,255,.25)}
.copy{left:0;width:1200px;top:3228px;text-align:center;font-size:13.5px;color:#fff}
.to-top{left:1116px;top:3184px;width:40px;height:40px;border-radius:50%;background:var(--orange);display:flex;align-items:center;justify-content:center}
</style>
</head>
<body>

<!-- header & hero -->
<div class="abs hero-bg"></div>
<div class="abs globe" role="img" aria-label="Translucent digital globe made of blue and gold circuit lines over a faint circuit-board background"></div>

<div class="abs logo"><span class="dot"></span>NOVA TECHNOLOGY</div>
<a class="abs nav active" style="left:713px">HOME</a>
<a class="abs nav" style="left:785px">ABOUT US</a>
<a class="abs nav" style="left:884px">SERVICES</a>
<a class="abs btn orange" style="left:966px;top:32px;width:132px">CONTACT US</a>

<h1 class="abs hero-title">EMPOWERING BUSINESSES WITH<br>HIGH-TECH SOLUTIONS</h1>
<p class="abs hero-sub">Professional IT services tailored for your business needs.</p>
<a class="abs btn orange" style="left:458px;top:415px;width:132px">LEARN MORE</a>
<a class="abs btn navy" style="left:598px;top:415px;width:132px">CONTACT US</a>

<!-- about -->
<div class="abs about-photo" role="img" aria-label="Two IT professionals reviewing work on a laptop together"></div>
<p class="abs about-kicker">ABOUT</p>
<h2 class="abs about-title">NOVA TECHNOLOGY<br>SERVICES</h2>
<p class="abs about-text">Nova Technology Services specializes in providing cutting-edge technology solutions to help businesses thrive in a rapidly evolving digital landscape. With a focus on professionalism, simplicity, and innovation, we are your trusted partner for all your tech needs.</p>

<!-- services -->
<h2 class="abs section-title" style="top:1112px">OUR SERVICES</h2>

<div class="abs card" style="left:143px;top:1192px">
  <div class="icon"><svg viewBox="0 0 32 32"><rect x="5" y="6" width="22" height="15" rx="2"/><path d="M11 26h10M16 21v5"/><path d="M9 17l4-4 3 3 6-6"/></svg></div>
  <h3>IT CONSULTING</h3>
  <p>Providing expert advice to<br>optimize your technology<br>strategies and achieve<br>business goals.</p>
</div>
<div class="abs card active" style="left:453px;top:1192px">
  <div class="icon navy"><svg viewBox="0 0 32 32"><path d="M7 18v-3a9 9 0 0 1 18 0v3"/><rect x="5" y="17" width="5" height="8" rx="2"/><rect x="22" y="17" width="5" height="8" rx="2"/><path d="M25 25c0 2-3 3-7 3"/></svg></div>
  <h3>IT SERVICES</h3>
  <p>Comprehensive IT support<br>and maintenance to<br>ensure your systems run<br>smoothly 24/7.</p>
</div>
<div class="abs card" style="left:760px;top:1192px">
  <div class="icon"><svg viewBox="0 0 32 32"><path d="M10 21a5 5 0 0 1-.5-10 7 7 0 0 1 13.5 1.5A4.3 4.3 0 0 1 22.5 21Z"/><path d="M12 21v5M16 21v6M20 21v5"/></svg></div>
  <h3>CLOUD SOLUTIONS</h3>
  <p>Seamless migration and<br>management of your<br>business operations on<br>the cloud.</p>
</div>
<div class="abs card" style="left:143px;top:1457px">
  <div class="icon"><svg viewBox="0 0 32 32"><path d="M16 4l10 4v7c0 7-5 11-10 13-5-2-10-6-10-13V8Z"/><path d="M11.5 16l3.5 3.5 6-6.5"/></svg></div>
  <h3>CYBERSECURITY</h3>
  <p>Advanced solutions to<br>protect your business<br>from cyber threats and<br>vulnerabilities.</p>
</div>
<div class="abs card" style="left:453px;top:1457px">
  <div class="icon"><svg viewBox="0 0 32 32"><rect x="4" y="6" width="24" height="18" rx="2"/><path d="M4 11h24M12 15l-3 3 3 3M20 15l3 3-3 3M17 14l-2 8"/></svg></div>
  <h3>DEVELOPMENT</h3>
  <p>Custom software<br>tailored to meet your<br>unique business<br>requirements.</p>
</div>
<div class="abs card" style="left:760px;top:1457px">
  <div class="icon"><svg viewBox="0 0 32 32"><path d="M5 27h22M9 27V18M14 27V13M19 27V16M24 27V9"/><path d="M7 13l6-5 5 3 7-6"/></svg></div>
  <h3>DATA ANALYTICS</h3>
  <p>Transforming data<br>into actionable<br>insights to drive<br>smarter decisions.</p>
</div>

<!-- who we serve -->
<div class="abs serve-photo" role="img" aria-label="Professional in a white shirt and glasses working on a laptop in a bright modern office"></div>
<h2 class="abs serve-title">WHO WE SERVE</h2>
<p class="abs serve-text">At Nova Technology Services, we cater to business customers (B2B) across various industries, including finance, healthcare, education, and retail.</p>

<!-- contact -->
<h2 class="abs section-title" style="top:2356px">GET IN TOUCH WITH US</h2>
<p class="abs contact-sub">Have questions? Need assistance? Reach out to us, and our team<br>will be happy to help!</p>
<div class="abs field" style="left:350px;top:2478px;width:246px;height:48px">Name</div>
<div class="abs field" style="left:604px;top:2478px;width:246px;height:48px">Email</div>
<div class="abs field" style="left:350px;top:2535px;width:500px;height:48px">Phone</div>
<div class="abs field area" style="left:352px;top:2592px;width:497px;height:156px">Message</div>
<a class="abs btn orange" style="left:431px;top:2775px;width:132px;height:40px;font-size:12px">SUBMIT</a>
<a class="abs btn navy" style="left:572px;top:2775px;width:180px;height:40px;font-size:12px">SCHEDULE A MEETING</a>

<!-- footer -->
<svg class="abs footer" viewBox="0 0 1200 370" aria-hidden="true">
  <path d="M0 96 Q600 -60 1200 96 L1200 370 L0 370 Z" fill="#0b4a6c"/>
</svg>
<div class="abs f-logo"><span class="dot"></span>NOVA TECHNOLOGY</div>

<p class="abs f-head" style="left:425px;top:3010px">USEFUL LINKS</p>
<ul class="abs f-links" style="top:3035px">
  <li>Home</li><li>About Us</li><li>Services</li><li>Contact Us</li>
</ul>

<p class="abs f-head" style="left:640px;top:3010px">CONTACT US</p>
<ul class="abs f-contact" style="top:3040px">
  <li><svg width="12" height="14" viewBox="0 0 12 14"><path d="M6 0a5 5 0 0 0-5 5c0 4 5 9 5 9s5-5 5-9a5 5 0 0 0-5-5zm0 7a2 2 0 1 1 0-4 2 2 0 0 1 0 4z" fill="#f7a935"/></svg>48 Circuit Lane, Business City</li>
  <li><svg width="12" height="14" viewBox="0 0 12 14"><rect x="0" y="3" width="12" height="9" rx="1" fill="#f7a935"/><path d="M0 4l6 4 6-4" stroke="#0b4a6c" fill="none"/></svg>contact@novatechservices.com</li>
  <li><svg width="12" height="14" viewBox="0 0 12 14"><path d="M2 1l3 0 1 3-2 1.5a7 7 0 0 0 3.5 3.5L9 7l3 1v3c-6 1-11-4-10-10z" fill="#f7a935"/></svg>+1 (555) 014-2290</li>
</ul>

<span class="abs social" style="left:965px"></span>
<span class="abs social" style="left:999px"></span>
<span class="abs social" style="left:1034px"></span>
<span class="abs social" style="left:1069px"></span>

<div class="abs rule"></div>
<p class="abs copy">© 2025 Nova Technology Services. All Rights Reserved.</p>
<a class="abs to-top" aria-label="Back to top"><svg width="12" height="8" viewBox="0 0 12 8"><path d="M1 7l5-5 5 5" stroke="#fff" stroke-width="2" fill="none"/></svg></a>

</body>
</html>
```